Project, Programme and Portfolio Management Consultant needs a business card

I have recently had someone create a brand guide for me and I wish to have new business cards that incorporate the new brand. I am an independent management consultant working with businesses to improve their ability to deliver their business strategy through selecting the right project, the right people and doing it in the right way. Whilst I am currently working on my own, I am hoping to start to build win business where I need to bring in a team and this branding activity is the start of that process.

Target Market(s)

Medium to large businesses, government departments and defence

Contact Information for Business Card

Name
job title
business name
mobile
email
website
linkedIn profile

Font styles to use
Other font styles liked:
• roboto light

Colors

Designer to choose colors to be used in the design.

Requirements
Must have
• Must use my logo and brand colours (see attached brand guide)

```html
<!DOCTYPE html>
<html lang="en">
<head>
<meta charset="utf-8">
<title>Quartwell Business Card</title>
<link rel="stylesheet" href="https://fonts.googleapis.com/css2?family=Open+Sans:wght@400;600&family=Montserrat:wght@500&display=swap">
<style>
  :root {
    --stage: #33495e;
    --stage-deep: #1e2c3a;
    --navy: #0d3a6b;
    --navy-ink: #1b2a4a;
    --paper: #ffffff;
    --teal: #2bb3a6;
    --gold: #e3b23c;
    --muted: #4b5a72;
  }
  * { box-sizing: border-box; margin: 0; padding: 0; }
  html, body { width: 1200px; height: 900px; overflow: hidden; }
  body {
    position: relative;
    background: radial-gradient(circle at 40% 40%, var(--stage), var(--stage-deep));
    font-family: "Open Sans", Arial, sans-serif;
  }
  .card {
    position: absolute;
    width: 560px;
    height: 320px;
    border-radius: 24px;
    overflow: hidden;
    box-shadow: 0 18px 40px rgba(0, 0, 0, 0.35);
  }
  /* Back side */
  .card-back {
    left: 570px; top: 90px;
    background: linear-gradient(135deg, #0f4279, var(--navy));
    display: flex; align-items: center; justify-content: center;
  }
  .brand {
    display: flex; align-items: center; gap: 14px;
    font-family: "Montserrat", Arial, sans-serif;
    font-weight: 500;
    letter-spacing: 6px;
    text-transform: uppercase;
  }
  .card-back .brand { color: var(--teal); font-size: 34px; }
  .brand-dot { border-radius: 50%; background: var(--gold); }
  .card-back .brand-dot { width: 22px; height: 22px; }

  /* Front side */
  .card-front {
    left: 70px; top: 480px;
    background: var(--paper);
  }
  .front-band {
    position: absolute; left: 0; right: 0; bottom: 0;
    height: 38px; background: var(--navy);
  }
  .identity { position: absolute; left: 34px; top: 32px; }
  .person-name {
    font-size: 24px; font-weight: 600; letter-spacing: 1px;
    color: var(--navy-ink);
  }
  .job-title {
    font-size: 11px; letter-spacing: 1.5px; color: var(--muted);
    margin-top: 2px;
  }
  .divider {
    position: absolute; left: 120px; right: 30px; top: 76px;
    height: 1.5px; background: var(--navy-ink);
  }
  .contact-list {
    position: absolute; left: 34px; top: 100px;
    list-style: none; font-size: 12px; color: var(--navy-ink);
  }
  .contact-list li, .web-list li {
    display: flex; align-items: center; gap: 8px; margin-bottom: 8px;
  }
  .icon { width: 12px; height: 12px; flex: none; }
  .card-front .brand {
    position: absolute; right: 40px; top: 130px;
    color: var(--navy-ink); font-size: 22px; letter-spacing: 4px; gap: 10px;
  }
  .card-front .brand-dot { width: 16px; height: 16px; }
  .web-list {
    position: absolute; right: 34px; bottom: 52px;
    list-style: none; font-size: 12.5px; font-weight: 600; color: var(--navy-ink);
    text-align: right;
  }
  .web-list li { justify-content: flex-end; }
</style>
</head>
<body>
  <section class="card card-back" aria-label="Card back">
    <div class="brand"><span class="brand-dot"></span>Quartwell</div>
  </section>

  <section class="card card-front" aria-label="Card front">
    <div class="identity">
      <p class="person-name">YOUR NAME</p>
      <p class="job-title">JOB TITLE</p>
    </div>
    <div class="divider"></div>

    <ul class="contact-list">
      <li>
        <svg class="icon" viewBox="0 0 12 12"><rect width="12" height="12" rx="2" fill="#1b2a4a"/><path d="M3.5 3h1.5l.7 1.7-.9.6a4 4 0 0 0 2 2l.6-.9 1.7.7V8.7A.8.8 0 0 1 8.3 9.5 5.5 5.5 0 0 1 2.5 3.7.8.8 0 0 1 3.5 3z" fill="#fff"/></svg>
        000 000 0000
      </li>
      <li>
        <svg class="icon" viewBox="0 0 12 12"><rect width="12" height="12" rx="2" fill="#1b2a4a"/><path d="M2.5 3.5h7v5h-7z M2.5 3.5 6 6.3 9.5 3.5" fill="none" stroke="#fff" stroke-width="1"/></svg>
        youremail@xyz.com
      </li>
    </ul>

    <div class="brand"><span class="brand-dot"></span>Quartwell</div>

    <ul class="web-list">
      <li>
        www.website.com
        <svg class="icon" viewBox="0 0 12 12"><circle cx="6" cy="6" r="5.3" fill="none" stroke="#1b2a4a"/><path d="M.7 6h10.6M6 .7c-3 3-3 7.6 0 10.6M6 .7c3 3 3 7.6 0 10.6" fill="none" stroke="#1b2a4a" stroke-width=".8"/></svg>
      </li>
      <li>
        /profile.link
        <svg class="icon" viewBox="0 0 12 12"><rect width="12" height="12" rx="2" fill="#1b2a4a"/></svg>
      </li>
    </ul>

    <div class="front-band"></div>
  </section>
</body>
</html>
```